ALL TEXT GRAPHICS TM May 2025 for Instagram

We are looking for a series of social media graphics for Instagram (new size: 4:5 (1080 x 1350 pixels) ratio that are ALL TEXT. We want the following quotes below on each graphic; one quote per graphic. AND, In very small letters at the bottom of each graphic, add @TovaMarshOnline
The look and feel of these graphics should be complimentary to the color palette attached below; but keep them simple. But the design is up to you; at the end of this document, I provided various samples of all text graphics that I like as examples.
Target Market(s)
women looking to lose weight
Look and feel

```html
<!DOCTYPE html>
<html lang="en">
<head>
<meta charset="utf-8">
<title>Tova Marsh – Text Graphics Series</title>
<link rel="stylesheet" href="https://fonts.googleapis.com/css2?family=Cinzel:wght@400;500&family=Marcellus&family=Bodoni+Moda:wght@400;500&family=Playball&family=Montserrat:wght@800&display=swap">
<style>
  :root {
    --page: #eeeeee;
    --card: #ffffff;
    --blush: #fbd0e7;
    --pink-deep: #d4086c;
    --pink: #ec2a8c;
    --pink-soft: #f27bb8;
    --ink: #3b3838;
  }
  * { margin: 0; padding: 0; box-sizing: border-box; }
  html, body { width: 986px; height: 1200px; overflow: hidden; background: var(--page); }
  .sheet { position: relative; width: 986px; height: 1200px; }

  .post {
    position: absolute;
    width: 277px; height: 346px;
    background-color: var(--card);
    text-align: center;
    overflow: hidden;
  }
  .glow-tl-br {
    background-image:
      radial-gradient(ellipse 70% 45% at 0% 0%, var(--blush), rgba(255,255,255,0) 100%),
      radial-gradient(ellipse 60% 40% at 100% 100%, var(--blush), rgba(255,255,255,0) 100%);
  }
  .glow-tr-bl {
    background-image:
      radial-gradient(ellipse 60% 40% at 100% 0%, var(--blush), rgba(255,255,255,0) 100%),
      radial-gradient(ellipse 70% 45% at 0% 100%, var(--blush), rgba(255,255,255,0) 100%);
  }

  .block { position: absolute; left: 0; right: 0; }

  .caps { font-family: "Cinzel", serif; letter-spacing: 0.04em; }
  .caps-light { font-family: "Marcellus", serif; letter-spacing: 0.06em; }
  .serif { font-family: "Bodoni Moda", serif; color: var(--ink); letter-spacing: 0.03em; }
  .script { font-family: "Playball", cursive; font-weight: 400; letter-spacing: 0; }
  .cta { font-family: "Montserrat", sans-serif; font-weight: 800; color: var(--pink); letter-spacing: 0.02em; }
  .handle {
    position: absolute; left: 0; right: 0;
    font-family: "Montserrat", sans-serif; font-weight: 800;
    font-size: 4.6px; letter-spacing: 0.04em; color: var(--ink);
  }

  .deep { color: var(--pink-deep); }
  .pink { color: var(--pink); }
  .soft { color: var(--pink-soft); }
</style>
</head>
<body>
<main class="sheet">

  <!-- Post 1 -->
  <section class="post glow-tl-br" style="left:47px; top:47px;">
    <div class="block" style="top:32px; line-height:27px;">
      <div class="caps deep" style="font-size:18px;">BLOATING.</div>
      <div class="script soft" style="font-size:22px;">Muffin top.</div>
      <div class="caps-light soft" style="font-size:17px;">PUFFY WAISTLINE.</div>
    </div>
    <div class="block serif" style="top:141px; font-size:22px; line-height:25.5px;">
      <div><span class="script soft">Your</span> body’s</div>
      <div>screaming</div>
      <div>for a <span class="script soft">different</span></div>
      <div>kind of Fix..</div>
    </div>
    <div class="block cta" style="top:292px; font-size:12.5px;">HERE IT IS</div>
    <div class="handle" style="top:324px;">@TOVAMARSHONLINE</div>
  </section>

  <!-- Post 2 -->
  <section class="post glow-tr-bl" style="left:356px; top:47px;">
    <div class="block serif" style="top:73px; font-size:19.5px; line-height:25.5px;">
      <div>You’re doing all</div>
      <div>the <span class="script pink">“right”</span> things,</div>
      <div>but your belly</div>
      <div>won’t <span class="script pink">go down?</span></div>
    </div>
    <div class="block serif" style="top:216px; font-size:19.5px; line-height:25.5px;">
      <div><span class="script pink">Here’s</span> what</div>
      <div>you haven’t <span class="caps-light pink" style="font-size:17px;">TRIED.</span></div>
    </div>
    <div class="handle" style="top:324px;">@TOVAMARSHONLINE</div>
  </section>

  <!-- Post 3 -->
  <section class="post glow-tl-br" style="left:665px; top:47px;">
    <div class="block" style="top:32px; line-height:26px;">
      <div class="caps deep" style="font-size:21px;">THE STUBBORN</div>
      <div class="caps pink" style="font-size:21px;">BELLY FAT</div>
      <div class="caps-light soft" style="font-size:18px;">AFTER 40?</div>
    </div>
    <div class="block serif" style="top:142px; font-size:22px; line-height:25px;">
      <div>It’s not</div>
      <div>about <span class="script soft">calories;</span></div>
      <div>it’s about</div>
      <div>your <span class="script soft">hormones.</span></div>
    </div>
    <div class="block cta" style="top:290px; font-size:12.5px;">HERE IS THE FIX.</div>
    <div class="handle" style="top:324px;">@TOVAMARSHONLINE</div>
  </section>

  <!-- Post 4 -->
  <section class="post glow-tr-bl" style="left:47px; top:423px;">
    <div class="block caps-light pink" style="top:82px; font-size:21px; line-height:27px;">
      <div>Your belly isn’t fat...</div>
      <div>it’s <span class="script deep" style="font-size:23px;">hormonal.</span></div>
      <div>And here’s</div>
      <div>how to <span class="script soft" style="font-size:23px;">Fix it.</span></div>
    </div>
    <div class="block serif" style="top:229px; font-size:17px; line-height:21px;">
      <div>Comment <span class="cta" style="font-size:16px;">HORMONES</span></div>
      <div>if nothing is working.</div>
    </div>
    <div class="handle" style="top:325px;">@TOVAMARSHONLINE</div>
  </section>

  <!-- Post 5 -->
  <section class="post glow-tl-br" style="left:354px; top:423px;">
    <div class="block" style="top:32px; line-height:28px;">
      <div class="caps-light deep" style="font-size:23px;">THAT</div>
      <div class="script pink" style="font-size:31px;">Stubborn</div>
      <div class="caps-light soft" style="font-size:23px;">WEIGHT?</div>
    </div>
    <div class="block serif" style="top:134px; font-size:22px; line-height:26px;">
      <div>It’s not <span class="script pink">your</span> fault.</div>
      <div>Your hormones</div>
      <div>are to <span class="script pink">blame</span></div>
      <div>and you’re not</div>
      <div class="script pink">Alone;</div>
    </div>
    <div class="block cta" style="top:293px; font-size:12.5px;">BUT THERE IS A FIX.</div>
    <div class="handle" style="top:328px;">@TOVAMARSHONLINE</div>
  </section>

  <!-- Post 6 -->
  <section class="post glow-tr-bl" style="left:662px; top:423px;">
    <div class="block" style="top:33px; line-height:26px;">
      <div class="caps deep" style="font-size:23px; font-weight:500;">TIRED.</div>
      <div class="caps pink" style="font-size:23px; font-weight:500;">MOODY.</div>
      <div class="caps-light soft" style="font-size:20px; line-height:22px;">STUBBORN<br>BELLY FAT.</div>
    </div>
    <div class="block serif" style="top:157px; font-size:26px; line-height:30px;">
      <div>Your <span class="script soft">Hormones</span></div>
      <div>are screaming</div>
      <div>for <span class="script soft">help!</span></div>
    </div>
    <div class="block cta" style="top:286px; font-size:14px; letter-spacing:0;">Let’s fix that.</div>
    <div class="handle" style="top:326px;">@TOVAMARSHONLINE</div>
  </section>

  <!-- Post 7 -->
  <section class="post glow-tl-br" style="left:45px; top:803px;">
    <div class="block caps-light soft" style="top:73px; font-size:22px; line-height:27px;">
      <div>Flat tummy in</div>
      <div><span class="script deep" style="font-size:24px;">your</span> 40s?</div>
      <div>It’s still <span class="script deep" style="font-size:24px;">possible!</span></div>
    </div>
    <div class="block serif" style="top:209px; font-size:16px; line-height:20px;">
      <div>Comment <span class="cta soft" style="font-size:15px;">BYE BELLY</span></div>
      <div>to get the 10 secrets</div>
      <div>to a <span class="script pink" style="font-size:17px;">Flatter tummy</span></div>
    </div>
    <div class="handle" style="top:331px;">@TOVAMARSHONLINE</div>
  </section>

</main>
</body>
</html>
```